Cafe - A FRAME Design

Need to create an A frame for my café.
Logo available
Word document - has basic information we think would be good.

Name: Zorvette Café

Notes from the A-frame printers.
File Requirements
• PDF without trim, crop or registration marks
• All files to be CMYK, not RGB
• All fonts converted to outlines (paths/curves)
• Embed all images and elements
• Files to be 100% scale unless otherwise specified
• 10mm Bleed
Resolution
• Bitmap images no less than 130 DPI at full size
Pantone Colours
• If required Pantone colours must be supplied

Target Market(s)

Mainly Students - University cafe

Requirements
Must have
• Cafe name: Zorvette
Nice to have
• Might be nice to have background - that orange color same as logo - just an idea

Word document - has basic idea regarding text that should be included

```html
<!DOCTYPE html>
<html lang="en">
<head>
<meta charset="utf-8">
<title>Zorvette Café – A-Frame Poster</title>
<link href="https://fonts.googleapis.com/css2?family=Montserrat:wght@400;700&family=Poppins:wght@500;600;700&display=swap" rel="stylesheet">
<style>
  :root {
    --orange: #f0592a;
    --orange-deep: #e24a1c;
    --orange-light: #f68a4c;
    --ink: #3f4450;
    --paper: #ffffff;
    --paper-grey: #eeeeef;
    --divider: #4a4e57;
    --scene-cream: #f6e6cc;
    --scene-wood: #c88a4a;
    --scene-green: #3f7a5a;
  }
  * { box-sizing: border-box; margin: 0; padding: 0; }
  html, body { width: 695px; height: 1200px; overflow: hidden; }
  body {
    background: var(--paper);
    font-family: "Poppins", sans-serif;
    color: var(--ink);
  }
  .poster {
    position: relative;
    width: 695px;
    height: 1200px;
    overflow: hidden;
    background:
      radial-gradient(circle at 80% 65%, var(--paper) 0%, rgba(255,255,255,0) 55%),
      linear-gradient(135deg, var(--paper-grey) 0%, #f8f8f8 40%, var(--paper) 70%, #f4f4f5 100%);
  }

  /* Brand */
  .brand {
    position: absolute;
    top: 80px;
    left: 0;
    width: 100%;
    display: flex;
    align-items: center;
    justify-content: center;
    gap: 22px;
  }
  .brand-dot {
    width: 74px;
    height: 74px;
    border-radius: 50%;
    background: var(--orange);
  }
  .brand-name {
    font-family: "Poppins", sans-serif;
    font-weight: 600;
    font-size: 84px;
    line-height: 1;
    color: var(--ink);
    letter-spacing: -1px;
  }

  /* Headline */
  .headline {
    position: absolute;
    top: 262px;
    width: 100%;
    text-align: center;
    font-family: "Montserrat", sans-serif;
    font-weight: 400;
    font-size: 36px;
    line-height: 1.3;
    color: var(--ink);
  }
  .headline strong { font-weight: 700; color: var(--orange); }

  /* Offer icons */
  .offers {
    position: absolute;
    top: 400px;
    left: 60px;
    right: 60px;
    display: flex;
    justify-content: space-between;
  }
  .offer {
    width: 160px;
    text-align: center;
  }
  .offer-icon {
    width: 106px;
    height: 106px;
    margin: 0 auto 12px;
    border-radius: 50%;
    background: radial-gradient(circle at 50% 30%, var(--orange-light), var(--orange-deep));
    border: 3px solid #d9431a;
    display: flex;
    align-items: center;
    justify-content: center;
  }
  .offer-icon svg { width: 64px; height: 64px; }
  .offer-label {
    font-weight: 600;
    font-size: 22px;
    line-height: 1.3;
    color: var(--ink);
  }
  .offer-divider {
    width: 0;
    height: 188px;
    border-left: 2px dashed var(--divider);
  }

  /* Banners */
  .banner-dark {
    position: absolute;
    top: 630px;
    left: 130px;
    width: 440px;
    height: 48px;
    background: var(--ink);
    clip-path: polygon(5% 0, 100% 0, 95% 100%, 0 100%);
    color: #fff;
    font-weight: 600;
    font-size: 24px;
    line-height: 48px;
    text-align: center;
  }
  .banner-orange {
    position: absolute;
    top: 678px;
    left: 207px;
    width: 290px;
    height: 46px;
    background: var(--orange);
    clip-path: polygon(0 0, 100% 0, 94% 100%, 6% 100%);
    color: #fff;
    font-weight: 700;
    font-size: 22px;
    line-height: 46px;
    text-align: center;
  }

  /* Scene area */
  .cafe-scene {
    position: absolute;
    top: 752px;
    left: 88px;
    width: 520px;
    height: 340px;
    border-radius: 36px 36px 60px 60px;
    background:
      linear-gradient(180deg, var(--scene-cream) 0%, var(--scene-cream) 55%, rgba(200,138,74,0.55) 78%, rgba(63,122,90,0.35) 100%);
  }

  /* Footer */
  .footer {
    position: absolute;
    left: 0;
    bottom: 0;
    width: 100%;
    height: 76px;
    background: var(--orange);
    color: #fff;
    font-weight: 700;
    font-size: 27px;
    line-height: 76px;
    text-align: center;
  }
</style>
</head>
<body>
  <main class="poster">
    <header class="brand">
      <span class="brand-dot"></span>
      <span class="brand-name">Zorvette</span>
    </header>

    <h1 class="headline">Your <strong>environmentally</strong><br>&amp; <strong>sustainability</strong> focused cafe</h1>

    <section class="offers">
      <div class="offer">
        <div class="offer-icon">
          <svg viewBox="0 0 64 64" fill="none" stroke="#fff" stroke-width="3" stroke-linecap="round" stroke-linejoin="round">
            <path d="M24 8c-3 4 3 6 0 10M32 8c-3 4 3 6 0 10M40 8c-3 4 3 6 0 10"/>
            <path d="M12 26h38v10a15 15 0 0 1-15 15h-8a15 15 0 0 1-15-15z"/>
            <path d="M50 30h3a6 6 0 0 1 0 12h-5"/>
            <path d="M8 56h48"/>
          </svg>
        </div>
        <div class="offer-label">Specialty<br>Coffee</div>
      </div>
      <div class="offer-divider"></div>
      <div class="offer">
        <div class="offer-icon">
          <svg viewBox="0 0 64 64" fill="none" stroke="#fff" stroke-width="3" stroke-linecap="round" stroke-linejoin="round">
            <path d="M8 34h48a24 18 0 0 1-48 0z"/>
            <path d="M20 34c0-8 6-12 12-12s12 4 12 12"/>
            <path d="M32 22c2-6 8-10 14-10-1 6-6 10-14 10z"/>
            <path d="M18 56h28"/>
          </svg>
        </div>
        <div class="offer-label">Fresh<br>Food</div>
      </div>
      <div class="offer-divider"></div>
      <div class="offer">
        <div class="offer-icon">
          <svg viewBox="0 0 64 64" fill="none" stroke="#fff" stroke-width="3" stroke-linecap="round" stroke-linejoin="round">
            <path d="M14 30a18 14 0 0 1 36 0z"/>
            <circle cx="32" cy="12" r="3"/>
            <path d="M12 30h40l-5 24H17z"/>
            <path d="M25 34l1 16M32 34v16M39 34l-1 16"/>
          </svg>
        </div>
        <div class="offer-label">Pastries<br>&amp; Drinks</div>
      </div>
    </section>

    <div class="banner-dark">(Vegan &amp; GF) options available</div>
    <div class="banner-orange">Catering Available</div>

    <div class="cafe-scene" role="img" aria-label="Illustration of a busy café interior with a counter, menu boards, hanging lamps, plants and guests at tables"></div>

    <footer class="footer">Located @ Building 418</footer>
  </main>
</body>
</html>
```